Flyer Jahreskonzert Gemischter Chor
Zielgruppe
Wir sind ein gemischter Chor aus der Schweiz unsere Mitglieder sind zwischen 20 und 70 Jahre jung und singen Querbeet durch die Musik von Lenz bis Velvix.
Das diesjährige Programm setzt sich aus Liedern von Gerd Palmow ( Schöne Grüße vom Hafen, Noch einmal ohne Zucker, nach 40 Wintern, Spanischer Mond, Klaus Wendlinger (Der bunte Garten), Gustav Rolf (Unter der Brücke), Walter Fischbeck(Tiefsee), und Miles Carver (Walk along the river slowly) zusammen.
Konzerttitel : 'Noch einmal ohne Zucker'
Daher würde ein 'süßes' Design passen, das ist aber nicht Bedingung, der Konzerttitel könnte auch noch angepasst werden.
Weitere Infos auf www.feierstimmen-beispiel.ch
Aufgabenstellung
Wir brauchen eine Vorderseite für einen Konzert Flyer Format A5 hochformat als Werbung für unser Jahreskonzert.
Text:
Konzert Feierstimmen Uerikon
Samstag 8. November 2014, 17:00Uhr
Uerikon/Stäfa
Singsaal Schulhaus Lindenhalde
Sonntag 9. November 2014, 17:00Uhr
Uetikon am See
Falkenhofsaal

```html
<!DOCTYPE html>
<html lang="de">
<head>
<meta charset="utf-8">
<title>Konzert Feierstimmen Uerikon</title>
<link rel="stylesheet" href="https://fonts.googleapis.com/css2?family=Lobster&family=Alfa+Slab+One&family=Arvo:wght@400;700&display=swap">
<style>
  :root {
    --flyer-pink: #e85c98;
    --cream-white: #ffffff;
    --berry-dark: #561126;
    --frosting: #f7d3df;
    --sponge: #7a4638;
    --liner: #f1e3ea;
  }
  html, body {
    margin: 0;
    padding: 0;
    width: 846px;
    height: 1200px;
    overflow: hidden;
    background: var(--flyer-pink);
  }
  .flyer {
    position: relative;
    width: 846px;
    height: 1200px;
    background: var(--flyer-pink);
    overflow: hidden;
  }
  .concert-title {
    position: absolute;
    inset: 0 auto auto 0;
    margin: 0;
    font-family: "Lobster", cursive;
    font-weight: 400;
    color: var(--cream-white);
    text-shadow: 4px 5px 6px rgba(90, 20, 45, 0.55);
    line-height: 1;
    white-space: nowrap;
  }
  .concert-title .line {
    position: absolute;
    display: block;
    font-size: 92px;
  }
  .concert-title .line-one { left: 66px; top: 52px; }
  .concert-title .line-two { left: 205px; top: 176px; }
  .cupcake-photo {
    position: absolute;
    left: 205px;
    top: 345px;
    width: 425px;
    height: 520px;
    border-radius: 46% 46% 22% 22% / 40% 40% 12% 12%;
    background: radial-gradient(ellipse 70% 55% at 50% 38%, var(--frosting) 0%, #f3c0d2 55%, rgba(243,192,210,0) 100%),
                linear-gradient(180deg, rgba(232,92,152,0) 0%, rgba(232,92,152,0) 50%, var(--sponge) 58%, #6a3a2e 66%, var(--liner) 72%, #ecdde5 100%);
    filter: blur(4px);
  }
  .concert-details {
    position: absolute;
    left: 138px;
    top: 900px;
    width: 572px;
    font-family: "Arvo", serif;
  }
  .concert-heading {
    margin: 0 0 18px;
    font-family: "Alfa Slab One", serif;
    font-weight: 400;
    font-size: 31px;
    line-height: 1.1;
    color: var(--berry-dark);
    display: flex;
    justify-content: space-between;
    white-space: nowrap;
  }
  .performance { margin-bottom: 20px; }
  .performance-date,
  .performance-place {
    display: flex;
    justify-content: space-between;
    white-space: nowrap;
  }
  .performance-date {
    font-size: 30px;
    font-weight: 400;
    color: var(--cream-white);
    line-height: 1.15;
  }
  .performance-place {
    font-size: 21px;
    color: var(--berry-dark);
    line-height: 1.3;
  }
  .performance-place.centered { justify-content: center; gap: 12px; }
  .website {
    position: absolute;
    left: 0;
    width: 846px;
    top: 1150px;
    text-align: center;
    font-family: "Arvo", serif;
    font-size: 16px;
    color: var(--cream-white);
  }
</style>
</head>
<body>
<main class="flyer">
  <h1 class="concert-title">
    <span class="line line-one">“... noch einmal</span>
    <span class="line line-two">ohne Zucker!“</span>
  </h1>

  <div class="cupcake-photo" role="img" aria-label="Foto eines Schokoladen-Cupcakes mit rosa Sahnehaube und Marzipanrose"></div>

  <section class="concert-details">
    <h2 class="concert-heading"><span>Konzert</span><span>Feierstimmen</span><span>Uerikon</span></h2>
    <div class="performance">
      <div class="performance-date"><span>Samstag 8. November 2014</span><span>|</span><span>17°° Uhr</span></div>
      <div class="performance-place"><span>Uerikon/Stäfa</span><span>|</span><span>Singsaal Schulhaus Lindenhalde</span></div>
    </div>
    <div class="performance">
      <div class="performance-date"><span>Sonntag 9. November 2014</span><span>|</span><span>17°° Uhr</span></div>
      <div class="performance-place centered"><span>Uetikon am See</span><span>|</span><span>Falkenhofsaal</span></div>
    </div>
  </section>

  <div class="website">www.feierstimmen-beispiel.ch</div>
</main>
</body>
</html>
```